Letterhead for Sell Sheets
Real Estate Agent
I need an updated 8.5 x 11 color letterhead for sell sheets and letters. Updated with a fresh look, full color bleed, and using my current logo and identifiers as inspiration.
Real Estate
Home sellers and owners and buyers
Creative and clean looking design.
personal logo
team photo
pwt logo
vilko balloon logo
plumeknots logo
head shot
current simple letterhead with correct addresses, phone numbers, etc
1 year old letterhead with awards and logos included
DUOB logo

```html
<!DOCTYPE html>
<html lang="en">
<head>
<meta charset="utf-8">
<title>Brivask Letterhead Set</title>
<link href="https://fonts.googleapis.com/css2?family=Tinos:ital,wght@0,400;0,700;1,400&family=Arimo:wght@400;700&display=swap" rel="stylesheet">
<style>
  :root {
    --canvas: #ffffff;
    --sheet: #ffffff;
    --band-light: #f1ede3;
    --band-mid: #ddd5c2;
    --band-dark: #b9ad92;
    --ink: #2a2724;
    --ink-soft: #5b554c;
    --photo-a: #3a3431;
    --photo-b: #c9c1b2;
    --fade: #efe9dc;
    --accent-red: #c8322c;
    --accent-blue: #2a4f8f;
    --accent-gold: #c99a2e;
  }
  * { margin: 0; padding: 0; box-sizing: border-box; }
  html, body { width: 1200px; height: 777px; overflow: hidden; background: var(--canvas); }
  .canvas { position: relative; width: 1200px; height: 777px; }
  .sheet {
    position: absolute; top: 4px; width: 590px; height: 771px;
    background: var(--sheet); box-shadow: 0 0 3px rgba(0,0,0,.25); overflow: hidden;
  }
  .sheet--team { left: 2px; }
  .sheet--agent { left: 606px; }
  .header-band { position: absolute; left: 0; top: 0; width: 590px; }
  .brand-name {
    position: absolute; font-family: "Tinos", serif; font-weight: 700;
    color: var(--ink); letter-spacing: 3px; display: flex; align-items: center; gap: 8px;
  }
  .brand-name .mark { width: 12px; height: 12px; background: var(--ink); display: inline-block; }
  .tagline { position: absolute; font-family: "Tinos", serif; font-style: italic; font-weight: 700; color: var(--ink); }
  .contact { position: absolute; font-family: "Arimo", sans-serif; color: var(--ink-soft); line-height: 1.5; }
  .photo { position: absolute; }
  .bottom-fade {
    position: absolute; left: 0; width: 590px;
    background: linear-gradient(to bottom, rgba(239,233,220,0), var(--fade));
  }
  .partners {
    position: absolute; left: 0; width: 590px; height: 40px;
    display: flex; justify-content: center; align-items: center; gap: 18px;
    font-family: "Arimo", sans-serif; font-weight: 700; font-size: 13px; color: var(--ink);
  }
  .partner-name { display: flex; align-items: center; gap: 5px; }
  .partner-name .mark { width: 10px; height: 10px; background: var(--accent-red); }
  .badge { display: inline-block; background: var(--band-dark); }
  .badge--round { width: 26px; height: 26px; border-radius: 50%; background: var(--ink); }
  .badge--small { width: 30px; height: 12px; }
  .footer-band {
    position: absolute; left: 0; bottom: 0; width: 590px; height: 26px;
    background: linear-gradient(to right, var(--band-mid), var(--band-light), var(--band-mid));
    font-family: "Tinos", serif; font-size: 14px; color: var(--ink);
    display: flex; align-items: center; justify-content: center;
  }
</style>
</head>
<body>
<div class="canvas">

  <section class="sheet sheet--team">
    <svg class="header-band" width="590" height="110" viewBox="0 0 590 110">
      <defs>
        <linearGradient id="bandTeam" x1="0" y1="0" x2="1" y2="0">
          <stop offset="0" stop-color="#d6cdb8"/>
          <stop offset=".55" stop-color="#efeadf"/>
          <stop offset="1" stop-color="#ddd5c2"/>
        </linearGradient>
      </defs>
      <path d="M0 0 H590 V14 Q585 92 500 96 H0 Z" fill="url(#bandTeam)"/>
      <path d="M0 96 H500 Q585 92 590 14" fill="none" stroke="#b9ad92" stroke-width="2"/>
    </svg>
    <div class="brand-name" style="left:48px; top:36px; font-size:38px;"><span class="mark"></span>BRIVASK</div>
    <div class="tagline" style="left:48px; top:100px; font-size:14px;">A Tradition of Trust in Ohio Real Estate</div>
    <div class="contact" style="left:260px; top:12px; font-size:9.5px;">
      412 N. Harlow Way, Dunmere, OH 43990<br>
      7720 Larkfield Court, Ostrand, OH 43872<br>
      Office (555) 210-4470 | Fax (555) 210-4471 | Nationwide (555) 300-1182<br>
      e-mail: tel@brivask.com
    </div>

    <div class="bottom-fade" style="top:540px; height:160px;"></div>
    <div class="photo" role="img" aria-label="Team photo of ten agents standing in a row"
         style="left:106px; top:583px; width:386px; height:106px; border-radius:40px 40px 0 0;
                background: linear-gradient(to bottom, var(--photo-b), var(--photo-a) 45%, var(--photo-a));"></div>

    <div class="partners" style="top:696px;">
      <span class="partner-name"><span class="mark"></span>Vilko Masters</span>
      <span class="badge badge--small"></span>
      <span class="badge badge--small"></span>
      <span class="badge badge--round"></span>
      <span class="badge badge--round" style="background:var(--accent-blue);"></span>
      <span class="partner-name" style="color:var(--accent-gold);">Plumeknots</span>
    </div>
    <div class="footer-band">www.brivask.com</div>
  </section>

  <section class="sheet sheet--agent">
    <svg class="header-band" width="590" height="240" viewBox="0 0 590 240">
      <defs>
        <linearGradient id="bandAgent" x1="0" y1="0" x2="1" y2="0">
          <stop offset="0" stop-color="#efeadf"/>
          <stop offset=".5" stop-color="#e6dfcf"/>
          <stop offset="1" stop-color="#cfc5ae"/>
        </linearGradient>
      </defs>
      <path d="M0 0 H590 V20 Q588 215 500 222 H0 Z" fill="url(#bandAgent)"/>
      <path d="M0 222 H500 Q588 215 590 20" fill="none" stroke="#b9ad92" stroke-width="2"/>
    </svg>
    <div class="photo" role="img" aria-label="Head shot of the agent in a dark suit"
         style="left:10px; top:8px; width:160px; height:196px;
                background: linear-gradient(to bottom, #e9e4da 0%, #cbbfae 35%, var(--photo-a) 60%);"></div>
    <div class="brand-name" style="left:228px; top:52px; font-size:44px;"><span class="mark"></span>BRIVASK</div>
    <div class="tagline" style="left:222px; top:126px; font-size:16px;">A Tradition of Trust in Ohio Real Estate</div>
    <div class="contact" style="left:190px; top:150px; font-size:9.5px; text-align:left;">
      412 N. Harlow Way, Dunmere, OH 43990 | 7720 Larkfield Court, Ostrand, OH 43872<br>
      Office (555) 210-4470 | Fax (555) 210-4471 | Nationwide (555) 300-1182<br>
      e-mail: tel@brivask.com
    </div>

    <div class="bottom-fade" style="top:620px; height:80px;"></div>
    <div class="partners" style="top:696px;">
      <span class="partner-name"><span class="mark"></span>Vilko Masters</span>
      <span class="badge badge--small"></span>
      <span class="badge badge--small"></span>
      <span class="badge badge--round"></span>
      <span class="badge badge--round" style="background:var(--accent-blue);"></span>
      <span class="partner-name" style="color:var(--accent-gold);">Plumeknots</span>
    </div>
    <div class="footer-band">www.brivask.com</div>
  </section>

</div>
</body>
</html>
```